The First Annual Fernwick Legacy Gala

Something similar to the attached but an attention grabber. It needs to attract people with money to spend!

```html
<!DOCTYPE html>
<html lang="en">
<head>
<meta charset="utf-8">
<title>The First Annual Fernwick Legacy Gala</title>
<link rel="stylesheet" href="https://fonts.googleapis.com/css2?family=Barlow+Condensed:wght@500;600;700;800&family=Fira+Sans:wght@700;800;900&family=Fira+Sans+Condensed:wght@800;900&family=Hind:wght@400;500&display=swap">
<style>
  :root {
    --sky: #6b93c8;
    --mid: #4f77b0;
    --deep: #3a5e94;
    --box: #5b86c4;
    --pill: #3f6298;
    --accent: #5a85c2;
    --ink: #454545;
    --white: #ffffff;
  }
  * { margin: 0; padding: 0; box-sizing: border-box; }
  html, body { width: 848px; height: 1200px; overflow: hidden; background: var(--white); }
  .poster { position: relative; width: 848px; height: 1200px; overflow: hidden; background: var(--white); }
  .backdrop { position: absolute; inset: 0; }
  .abs { position: absolute; }

  .presents {
    left: 136px; top: 0; width: 580px; height: 54px;
    background: var(--white); border-radius: 0 0 14px 14px;
    display: flex; align-items: center; justify-content: center;
    font-family: "Fira Sans", sans-serif; font-weight: 800; font-size: 23px;
    color: var(--accent); letter-spacing: 0.2px;
  }
  .title {
    left: 0; top: 72px; width: 848px; text-align: center;
    font-family: "Fira Sans Condensed", sans-serif; font-weight: 900;
    color: var(--white); font-size: 76px; line-height: 94px;
    text-shadow: 3px 4px 4px rgba(20, 40, 80, 0.45);
  }

  .date {
    left: 357px; top: 388px; width: 192px; text-align: center;
    font-family: "Barlow Condensed", sans-serif; font-weight: 700;
    color: var(--white); font-size: 46px; line-height: 52px;
  }
  .starting {
    left: 566px; top: 428px;
    font-family: "Barlow Condensed", sans-serif; font-weight: 700;
    color: var(--white); font-size: 32px;
  }
  .time-badge {
    left: 712px; top: 387px; width: 72px; height: 72px; border-radius: 50%;
    background: var(--mid); display: flex; align-items: center; justify-content: center;
    font-family: "Barlow Condensed", sans-serif; font-weight: 700; font-size: 36px; color: var(--white);
  }
  .pm {
    left: 778px; top: 442px;
    font-family: "Barlow Condensed", sans-serif; font-weight: 700; font-size: 18px; color: var(--white);
  }
  .cocktail {
    left: 561px; top: 462px;
    font-family: "Barlow Condensed", sans-serif; font-weight: 700;
    color: var(--white); font-size: 34px;
  }

  .highlights {
    left: 376px; top: 552px; width: 440px;
    font-family: "Barlow Condensed", sans-serif; font-weight: 700;
    color: var(--accent); font-size: 35px; line-height: 37px;
  }
  .about {
    left: 376px; top: 636px; width: 420px;
    font-family: "Hind", sans-serif; font-weight: 400;
    color: var(--ink); font-size: 16.5px; line-height: 25.5px; text-align: justify;
  }
  .about p { margin-bottom: 15px; }
  .about p.gap { margin-top: 24px; }

  .ticket-box {
    left: 32px; width: 302px;
    background: var(--box); border: 2px dashed var(--white); border-radius: 8px;
    display: flex; flex-direction: column; justify-content: center; align-items: center;
    font-family: "Barlow Condensed", sans-serif; font-weight: 600;
    color: var(--white); font-size: 25px; line-height: 29px; text-align: center;
  }
  .ticket-box.event { top: 684px; height: 114px; }
  .ticket-box.raffle { top: 817px; height: 170px; }
  .price { background: var(--pill); border-radius: 7px; padding: 0 3px; }

  .social-mark {
    left: 157px; top: 1007px; width: 72px; height: 74px;
    border: 3px solid var(--white); border-radius: 9px; background: var(--mid);
  }
  .social-caption {
    left: 30px; top: 1094px; width: 306px; text-align: center;
    font-family: "Barlow Condensed", sans-serif; font-weight: 500;
    color: var(--white); font-size: 17px; line-height: 20px;
  }

  .tickets-panel {
    left: 368px; top: 943px; width: 480px; height: 257px;
    background: var(--mid); padding: 24px 16px 0 17px; color: var(--white);
  }
  .tickets-panel h3 {
    font-family: "Barlow Condensed", sans-serif; font-weight: 700; font-size: 21px; margin-bottom: 6px;
  }
  .tickets-panel .outlets {
    font-family: "Hind", sans-serif; font-weight: 500; font-size: 15px; line-height: 21.5px; margin-bottom: 26px;
  }
  .tickets-panel .contacts {
    font-family: "Barlow Condensed", sans-serif; font-weight: 500; font-size: 18.5px; margin-top: 10px;
  }
</style>
</head>
<body>
<div class="poster">

  <svg class="backdrop" width="848" height="1200" viewBox="0 0 848 1200" aria-hidden="true">
    <!-- dark left column -->
    <rect x="20" y="440" width="331" height="760" fill="var(--deep)"/>
    <!-- lower light band holding the time -->
    <path d="M350 360 C 560 345, 720 300, 848 250 V 486 C 760 515, 650 532, 520 532 L 350 532 Z" fill="var(--sky)"/>
    <!-- deep middle band -->
    <path d="M330 356 C 540 345, 710 300, 848 258 V 318 C 710 350, 560 380, 360 396 Z" fill="var(--mid)" stroke="var(--white)" stroke-width="4"/>
    <!-- top field -->
    <path d="M0 0 H848 V228 C 720 300, 540 352, 330 360 C 200 364, 90 390, 0 455 Z" fill="var(--sky)" stroke="var(--white)" stroke-width="5"/>
    <!-- header rules -->
    <line x1="0" y1="17" x2="848" y2="17" stroke="var(--white)" stroke-width="1.5"/>
    <line x1="0" y1="31" x2="848" y2="31" stroke="var(--white)" stroke-width="1.5"/>
    <!-- venue photo circle -->
    <circle cx="188" cy="482" r="172" fill="var(--white)"/>
    <circle cx="188" cy="482" r="163" fill="var(--sky)"/>
    <defs>
      <linearGradient id="venueTones" x1="0" y1="0" x2="0" y2="1">
        <stop offset="0" stop-color="#a9cdee"/>
        <stop offset="0.45" stop-color="#e9eef3"/>
        <stop offset="0.68" stop-color="#9aa68a"/>
        <stop offset="1" stop-color="#8e8a5e"/>
      </linearGradient>
    </defs>
    <circle cx="188" cy="482" r="153" fill="url(#venueTones)" role="img" aria-label="Photo of the white community center building with a metal roof on a grassy lot"/>
    <!-- date circle -->
    <circle cx="453" cy="424" r="104" fill="var(--white)"/>
    <circle cx="453" cy="424" r="96" fill="var(--mid)"/>
  </svg>

  <div class="abs presents">THE FERNWICK COMMUNITY CENTER PRESENTS</div>
  <h1 class="abs title">The First Annual Fernwick<br>Legacy Gala</h1>

  <div class="abs date">APRIL 23,<br>2022</div>
  <div class="abs starting">STARTING AT</div>
  <div class="abs time-badge">5:00</div>
  <div class="abs pm">PM</div>
  <div class="abs cocktail">WITH COCKTAIL HOUR</div>

  <h2 class="abs highlights">Live auction, silent auction, raffle and a cash bar!</h2>
  <div class="abs about">
    <p>Come on out to the Fernwick Community Center for a delicious prime rib dinner, drinks, entertainment and more! There will be plenty of amazing auction items for everyone to choose from.</p>
    <p>All proceeds will go to the Fernwick Community Center. We will share some history of the school and each year we will highlight a local family. This year will be the Harrow family who have been here for ....years!!</p>
    <p class="gap">High Side Barn, dirt bike, custom knives, a pack trip and so much more!</p>
  </div>

  <div class="abs ticket-box event">
    <div>TICKETS FOR THE EVENT</div>
    <div>ARE <span class="price">$50</span> EACH</div>
    <div>OR <span class="price">$90</span> FOR A COUPLE</div>
  </div>
  <div class="abs ticket-box raffle">
    <div>TICKETS FOR THE 10X12</div>
    <div>HIGH SIDE BARN <span class="price">$25</span> EACH</div>
    <div>OR 5 FOR <span class="price">$100.</span> DONATED</div>
    <div>BY: RIDGELINE SHED CO.</div>
    <div>OF ALDER FALLS, VALUE <span class="price">$6500</span></div>
  </div>

  <div class="abs social-mark" aria-hidden="true"></div>
  <p class="abs social-caption">Fernwick Community Center's Townboard page to see all the auction items available!</p>

  <section class="abs tickets-panel">
    <h3>Get your tickets from:</h3>
    <p class="outlets">Ridgeline Shed Co. in Alder Falls 48 Quarry Ln, Alder Falls Summit Crest Realty 212 E Cedar St, Alder Falls Fernwick Store 6410 Route 88, Fernwick</p>
    <h3>Or get them from</h3>
    <p class="contacts">Dana Morrow -(555)014-2287&nbsp;&nbsp;Jess Calder -(555)018-4493</p>
  </section>

</div>
</body>
</html>
```